AI Business Tools Landing Page

My web-based website builder (Nurvanta.com) will be adding many new features in the very near future and I need an eye-catching landing page to promote these new products.

The page will have a primary section of the 8 main products we are promoting:
1. AI Instant Website Generator
2. AI Chatbot
3. Online Store Builder with AI Assistance
4. AI Auto-Blogging System
5. Online Scheduling System
6. Custom Email System
7. SEO Service
8. CRM System

The page will also have a smaller section for links to our affiliate programs. These can be smaller, less-promanent buttons or links. These are the affiliate products:
1. Get Your LLC
2. Website Design and Maintenance
3. Tavolin Ads Management
4. Social Media Posting Service
5. Logo Design
6. Trademark Registration
7. Patent Application
8. Printing Services (including postcards, flyers, and merch.)
9. Bulk AI Content Generator

The theme and color scheme of the page should follow the theme of our main website, which is https://nurvanta.com.

I need the page fully coded and ready to deploy on my server.

I look forward to seeing your amazing designs!

```html
<!DOCTYPE html>
<html lang="en">
<head>
<meta charset="UTF-8">
<title>Nurvanta — Additional Features &amp; Tools for Website</title>
<link href="https://fonts.googleapis.com/css2?family=Poppins:wght@300;400;500;600;700;800&display=swap" rel="stylesheet">
<style>
  :root{
    --navy:#0c1b3c;
    --hero-dark:#0a2560;
    --hero-mid:#123f8f;
    --sky:#29b6f6;
    --sky-soft:#d6effc;
    --ink:#111827;
    --text:#2b2f38;
    --card-border:#bfe3f7;
    --button-text:#26a9e6;
    --panel:#f3f5f9;
    --white:#ffffff;
  }
  *{box-sizing:border-box;margin:0;padding:0}
  html,body{width:1200px;height:2356px;overflow:hidden;background:var(--white)}
  body{font-family:'Poppins',sans-serif;color:var(--text);position:relative}

  /* Hero */
  .hero{position:absolute;left:0;top:0;width:1200px;height:680px;overflow:hidden;
    background:radial-gradient(circle at 65% 30%,#1c56b0 0%,var(--hero-mid) 35%,var(--hero-dark) 80%)}
  .hero-wedge{position:absolute;left:0;top:0;width:1200px;height:680px}
  .brand{position:absolute;display:flex;align-items:center;gap:10px;color:var(--white);font-weight:600}
  .brand-dot{width:34px;height:34px;border-radius:50%;background:var(--sky)}
  .hero .brand{left:128px;top:26px;font-size:31px}
  .hero-eyebrow{position:absolute;left:124px;top:224px;font-size:22px;font-weight:300;color:var(--sky);display:flex;align-items:center;gap:10px}
  .hero-eyebrow::after{content:"";width:36px;height:1.5px;background:var(--sky)}
  .hero-title{position:absolute;left:118px;top:266px;color:var(--white);line-height:1.2}
  .hero-title strong{display:block;font-size:46px;font-weight:800}
  .hero-title span{display:block;font-size:46px;font-weight:400}
  .hero-art{position:absolute;left:560px;top:90px;width:620px;height:500px;border-radius:48% 52% 40% 40%;
    background:radial-gradient(circle at 35% 35%,rgba(80,170,255,.55),rgba(41,182,246,.25) 45%,rgba(18,63,143,0) 72%)}
  .hero-line{position:absolute;left:613px;top:565px;width:1.5px;height:86px;background:var(--sky)}
  .hero-line::after{content:"";position:absolute;left:-4px;bottom:-8px;width:10px;height:10px;border-radius:50%;background:var(--sky)}

  /* Section titles */
  .section-title{position:absolute;left:0;width:1200px;text-align:center;font-size:32px;font-weight:400;color:var(--ink)}
  .section-title strong{font-weight:700}
  .features-title{top:700px}
  .features-title::after{content:"";position:absolute;left:579px;top:54px;width:76px;height:2.5px;background:var(--sky)}

  /* Feature cards */
  .features{position:absolute;left:80px;top:787px;width:1057px;display:grid;grid-template-columns:repeat(4,253px);gap:18px 15px}
  .card{border:1.5px solid var(--card-border);border-radius:6px;background:var(--white);padding:14px 16px 16px 0;height:387px}
  .row-two .card,.card.tall{height:420px}
  .card-art{margin:0 auto 14px 42px;width:180px;height:170px;border-radius:50%;
    background:radial-gradient(circle at 50% 50%,#7fd0fb 0%,#bfe7fd 45%,#eaf7ff 70%,rgba(255,255,255,0) 72%)}
  .card-art.deep{background:radial-gradient(circle,#1e4fc7 0%,#1a3fa8 55%,#29b6f6 66%,rgba(255,255,255,0) 68%)}
  .card-title{border-left:3px solid var(--sky);padding-left:32px;font-size:15.5px;font-weight:600;color:var(--ink);line-height:1.3;margin-bottom:12px}
  .card-list{list-style:none;padding-left:32px}
  .card-list li{position:relative;padding-left:26px;font-size:11px;line-height:1.2;color:var(--text);margin-bottom:22px}
  .card-list li::before{content:"";position:absolute;left:0;top:1px;width:17px;height:17px;border-radius:50%;background:var(--sky-soft)}
  .card-list li::after{content:"";position:absolute;left:5px;top:5px;width:7px;height:4px;border-left:1.8px solid var(--sky);border-bottom:1.8px solid var(--sky);transform:rotate(-45deg)}

  /* Tools */
  .tools-panel{position:absolute;left:0;top:1688px;width:1200px;height:520px;background:var(--panel)}
  .tools-title{top:1740px;font-size:30px}
  .tools{position:absolute;left:105px;top:1835px;display:grid;grid-template-columns:332px 330px 332px;gap:16px 14px}
  .tool{height:64px;border:1.5px solid #9fd6f3;border-radius:2px;background:var(--white);display:flex;flex-direction:column;align-items:center;justify-content:center;color:var(--button-text);font-size:16px;font-weight:600;text-decoration:none}
  .tool small{font-size:10.5px;font-weight:400;color:#6b7280}
  .tool.featured{background:var(--navy);border-color:var(--navy);color:var(--white)}

  /* Footer */
  .footer{position:absolute;left:0;top:2140px;width:1200px;height:216px}
  .footer svg{position:absolute;left:0;top:0}
  .footer .brand{left:100px;top:108px;font-size:32px}
  .copyright{position:absolute;left:0;width:1200px;top:136px;text-align:center;color:#dfe6f3;font-size:15px}
  .socials{position:absolute;left:892px;top:116px;display:grid;grid-template-columns:repeat(5,20px);gap:16px 17px}
  .socials span{width:20px;height:20px;border-radius:50%;background:var(--white)}
</style>
</head>
<body>

<header class="hero">
  <div class="hero-art" role="img" aria-label="Digital robot figure holding a glowing AI sphere"></div>
  <svg class="hero-wedge" viewBox="0 0 1200 680" aria-hidden="true">
    <polygon points="640,612 1200,565 1200,680" fill="#29b6f6"/>
    <polygon points="0,662 640,612 1200,680 0,680" fill="#ffffff"/>
  </svg>
  <div class="brand"><span class="brand-dot"></span>Nurvanta</div>
  <p class="hero-eyebrow">Nurvanta Features &amp; Tools</p>
  <h1 class="hero-title"><strong>Additional Features</strong><span>&amp; Tools for Website</span></h1>
  <div class="hero-line"></div>
</header>

<h2 class="section-title features-title">Additional Features <strong>for Your Website</strong></h2>

<section class="features">
  <article class="card">
    <div class="card-art" role="img" aria-label="Hand choosing a website template on a screen"></div>
    <h3 class="card-title">AI Instant Website Generator</h3>
    <ul class="card-list">
      <li>Get a professional, SEO-optimized website in seconds!</li>
      <li>Includes custom domain, secure high-speed hosting, professional images, and more!</li>
    </ul>
  </article>
  <article class="card">
    <div class="card-art deep" role="img" aria-label="Chatbot robot on a laptop"></div>
    <h3 class="card-title">AI ChatBot</h3>
    <ul class="card-list">
      <li>Fully-trainable ChatBot will learn about your business to automate the customer support process!</li>
      <li>Built-in CRM features integrate emailing, text messaging, and contact forms!</li>
    </ul>
  </article>
  <article class="card">
    <div class="card-art" role="img" aria-label="Isometric online storefront with payment cards"></div>
    <h3 class="card-title">Online Store Builder (E-Commerce) with AI Assistance</h3>
    <ul class="card-list">
      <li>Sell you products online and integrate your products into any website!</li>
      <li>Accept payments from multiple payment gateways including Payvane and Quillpay!</li>
    </ul>
  </article>
  <article class="card">
    <div class="card-art" role="img" aria-label="Blog pages generated by an AI blogging system"></div>
    <h3 class="card-title">AI Auto-Blogging System</h3>
    <ul class="card-list">
      <li>AI will generate an incredible blog for your business in seconds and immediately begin posting content for you!</li>
      <li>Choose from daily, weekly, or monthly automated blog posting. Consistent, unique, SEO-optimized content posting on cruise control!</li>
    </ul>
  </article>

  <article class="card tall">
    <div class="card-art deep" role="img" aria-label="Tablet showing a monthly scheduling calendar"></div>
    <h3 class="card-title">Online Scheduling System</h3>
    <ul class="card-list">
      <li>Get appointment bookings, restaurant reservations, or consultations scheduled directly from your website!</li>
      <li>Manage your employees' schedules and all your appointments from a simple, user-friendly dashboard!</li>
    </ul>
  </article>
  <article class="card tall">
    <div class="card-art" role="img" aria-label="Email inbox using a custom domain address"></div>
    <h3 class="card-title">Custom emails using your domain</h3>
    <ul class="card-list">
      <li>Quickly set up emails for yourself and all your employees with your own domain extension (example – johnd@yoursite.com). No more unprofessional Mailora and Zephmail email addresses!</li>
      <li>Manage all your business emails from a simple, user-friendly interface!</li>
    </ul>
  </article>
  <article class="card tall">
    <div class="card-art" role="img" aria-label="Laptop showing backlink building links"></div>
    <h3 class="card-title">SEO Service – Automatic Backlink Building</h3>
    <ul class="card-list">
      <li>Let us do the hard work of getting high-quality backlinks to your website. Although difficult to get, backlinks to your website boost search engine ranking more than any other strategy!</li>
      <li>Subscribe now and start getting 10-20 high-quality permanent backlinks to your website every month, guaranteed!</li>
    </ul>
  </article>
  <article class="card tall">
    <div class="card-art deep" role="img" aria-label="CRM dashboard with charts and data"></div>
    <h3 class="card-title">Customer Relationship Management (CRM) System</h3>
    <ul class="card-list">
      <li>Automate the lead follow up process to consistently stay in front of your potential customers!</li>
      <li>Schedule automatic email and text campaigns and effortlessly follow your funnels from lead to closing!</li>
    </ul>
  </article>
</section>

<div class="tools-panel"></div>
<h2 class="section-title tools-title">More Tools to Help You <strong>Grow Your Business</strong></h2>
<nav class="tools">
  <a class="tool" href="#">Get Your LLC</a>
  <a class="tool featured" href="#">Social Media Posting Service</a>
  <a class="tool" href="#">Patent Application</a>
  <a class="tool" href="#">Website Design and Maintenance</a>
  <a class="tool" href="#">Logo Design</a>
  <a class="tool" href="#">Printing Services<small>(including postcards, flyers, and merch.)</small></a>
  <a class="tool" href="#">Tavolin Ads Management</a>
  <a class="tool" href="#">Trademark Registration</a>
  <a class="tool" href="#">Bulk AI Content Generator</a>
</nav>

<footer class="footer">
  <svg width="1200" height="216" viewBox="0 0 1200 216" aria-hidden="true">
    <path d="M0,8 C200,0 380,30 600,40 C820,50 1000,40 1200,20 L1200,216 L0,216 Z" fill="#1ea5e9"/>
    <path d="M0,22 C220,16 420,62 640,70 C860,78 1040,60 1200,36 L1200,216 L0,216 Z" fill="var(--navy)"/>
  </svg>
  <div class="brand"><span class="brand-dot"></span>Nurvanta</div>
  <p class="copyright">© 2024 Nurvanta. All Rights Reserved</p>
  <div class="socials" aria-label="Social links">
    <span></span><span></span><span></span><span></span><span></span>
    <span></span><span></span><span></span><span></span><span></span>
  </div>
</footer>

</body>
</html>
```